Dunmore Acres Enterprise
Home grown grain fed beef Wholes, Halfs, Quarters
Locally raised
No Added Hormones
Call or text now to order (555) -0418-2957

```html
<!DOCTYPE html>
<html lang="en">
<head>
<meta charset="utf-8">
<title>Dunmore Acres Enterprise – Home Grown Grain Fed Beef</title>
<link href="https://fonts.googleapis.com/css2?family=Germania+One&family=Oswald:wght@500&family=Poppins:wght@700;800;900&display=swap" rel="stylesheet">
<style>
  :root {
    --ink: #141414;
    --paper: #f3f3f3;
    --paper-shade: #dcdcdc;
    --brand-red: #cf1d22;
    --leaf-green: #4b9a17;
    --badge-green: #4a9417;
    --sketch-grey: #c9c9c9;
    --meat-deep: #6e0f14;
    --meat-mid: #a3222a;
  }
  * { margin: 0; padding: 0; box-sizing: border-box; }
  html, body { width: 910px; height: 1200px; overflow: hidden; background: var(--paper); }
  .flyer {
    position: relative; width: 910px; height: 1200px; overflow: hidden;
    background:
      radial-gradient(ellipse at 20% 15%, rgba(0,0,0,0.05), transparent 45%),
      radial-gradient(ellipse at 85% 90%, rgba(0,0,0,0.07), transparent 50%),
      radial-gradient(ellipse at 10% 85%, rgba(0,0,0,0.06), transparent 40%),
      var(--paper);
  }
  .brand-mark {
    position: absolute; left: 0; top: 52px; width: 910px;
    display: flex; flex-direction: column; align-items: center;
  }
  .brand-mark__circle {
    width: 96px; height: 96px; border-radius: 50%;
    border: 3px solid var(--ink); background: transparent;
  }
  .brand-mark__name {
    margin-top: 10px;
    font-family: "Germania One", serif; font-size: 40px; color: var(--ink);
    letter-spacing: 1px; line-height: 1;
  }
  .headline {
    position: absolute; left: 0; width: 910px; text-align: center;
    font-family: "Germania One", serif; line-height: 1;
  }
  .headline--name { top: 246px; font-size: 124px; color: var(--ink); letter-spacing: 2px; }
  .headline--sub { top: 364px; font-size: 96px; color: var(--brand-red); letter-spacing: 1px; }
  .pasture-sketch {
    position: absolute; left: 0; top: 440px; width: 910px; height: 380px;
    background: radial-gradient(ellipse at 50% 45%, rgba(190,190,190,0.55), rgba(220,220,220,0.25) 55%, transparent 75%);
  }
  .beef-photo {
    position: absolute; left: 46px; top: 660px; width: 535px; height: 405px;
    border-radius: 46% 50% 42% 48% / 44% 46% 52% 50%;
    background: radial-gradient(ellipse at 55% 40%, var(--meat-mid), var(--meat-deep) 75%);
  }
  .raised-arc { position: absolute; left: 0; top: 0; width: 910px; height: 1200px; pointer-events: none; }
  .raised-arc text {
    font-family: "Poppins", sans-serif; font-weight: 900; font-size: 40px;
    fill: var(--leaf-green); letter-spacing: 1px;
  }
  .hormone-badge { position: absolute; left: 68px; top: 873px; width: 156px; height: 156px; }
  .hormone-badge__text {
    position: absolute; inset: 0; display: flex; align-items: center; justify-content: center;
    text-align: center; font-family: "Oswald", sans-serif; font-weight: 500;
    font-size: 27px; line-height: 1.15; color: #fff; text-transform: uppercase;
  }
  .beef-claim {
    position: absolute; left: 584px; top: 630px;
    font-family: "Poppins", sans-serif; font-weight: 900; font-size: 55px;
    line-height: 45px; color: var(--ink); letter-spacing: -1.5px; text-transform: uppercase;
  }
  .share-list { position: absolute; left: 586px; top: 845px; list-style: none; }
  .share-list__item {
    display: flex; align-items: center; width: 250px; height: 51px; margin-bottom: 9px;
    border-radius: 22px; background: var(--brand-red);
    font-family: "Poppins", sans-serif; font-weight: 800; font-size: 35px; color: #fff;
    text-transform: uppercase; letter-spacing: -0.5px;
  }
  .share-list__tick { width: 18px; height: 18px; margin: 0 8px 0 9px; flex: none; }
  .order-line {
    position: absolute; left: 0; width: 910px; top: 1096px;
    display: flex; align-items: center; justify-content: center;
    font-family: "Poppins", sans-serif; font-weight: 700; font-size: 26px;
    color: var(--ink); text-transform: uppercase;
  }
  .order-line__accent { color: var(--brand-red); margin-left: 8px; }
  .order-line__icon { width: 40px; height: 40px; margin: 0 14px 0 16px; }
  .order-line__phone { font-size: 30px; }
</style>
</head>
<body>
<main class="flyer">
  <header class="brand-mark">
    <span class="brand-mark__circle" aria-hidden="true"></span>
    <span class="brand-mark__name">Dunmore Acres</span>
  </header>

  <h1 class="headline headline--name">DUNMORE ACRES</h1>
  <p class="headline headline--sub">ENTERPRISE</p>

  <div class="pasture-sketch" role="img" aria-label="Faint pencil sketch of cattle grazing in a fenced pasture"></div>

  <div class="beef-photo" role="img" aria-label="Photo of raw beef chunks garnished with rosemary sprigs"></div>

  <svg class="raised-arc" viewBox="0 0 910 1200" aria-hidden="false">
    <path id="raisedCurve" d="M 192 700 Q 345 560 495 715" fill="none"/>
    <text><textPath href="#raisedCurve" startOffset="50%" text-anchor="middle">LOCALLY RAISED</textPath></text>
  </svg>

  <div class="hormone-badge">
    <svg viewBox="0 0 156 156" width="156" height="156" aria-hidden="true">
      <polygon fill="var(--badge-green)" points="78,0 87,10 99,3 104,16 118,13 118,27 132,28 128,41 141,47 133,58 144,67 133,76 141,87 129,93 134,107 120,109 120,123 106,122 102,136 90,130 82,142 72,133 61,141 55,128 41,132 39,118 25,116 29,102 16,96 24,85 13,76 24,67 16,56 29,50 24,37 38,34 37,20 51,22 54,8 66,14"/>
    </svg>
    <p class="hormone-badge__text">No Added<br>Hormones</p>
  </div>

  <h2 class="beef-claim">Home<br>Grown<br>Grain<br>Fed Beef</h2>

  <ul class="share-list">
    <li class="share-list__item">
      <svg class="share-list__tick" viewBox="0 0 18 18" aria-hidden="true"><circle cx="9" cy="9" r="9" fill="var(--ink)"/><path d="M5 9.2 L8 12 L13 6.5" fill="none" stroke="var(--brand-red)" stroke-width="2"/></svg>
      Wholes
    </li>
    <li class="share-list__item">
      <svg class="share-list__tick" viewBox="0 0 18 18" aria-hidden="true"><circle cx="9" cy="9" r="9" fill="var(--ink)"/><path d="M5 9.2 L8 12 L13 6.5" fill="none" stroke="var(--brand-red)" stroke-width="2"/></svg>
      Halfs
    </li>
    <li class="share-list__item">
      <svg class="share-list__tick" viewBox="0 0 18 18" aria-hidden="true"><circle cx="9" cy="9" r="9" fill="var(--ink)"/><path d="M5 9.2 L8 12 L13 6.5" fill="none" stroke="var(--brand-red)" stroke-width="2"/></svg>
      Quarters
    </li>
  </ul>

  <footer class="order-line">
    <span>Call or text now</span><span class="order-line__accent">to order</span>
    <svg class="order-line__icon" viewBox="0 0 40 40" aria-hidden="true">
      <circle cx="20" cy="20" r="20" fill="var(--leaf-green)"/>
      <path d="M13 11 c2-1 3 0 4 2 l1 3 c0 1-1 2-2 3 c1 3 3 5 6 6 c1-1 2-2 3-2 l3 1 c2 1 3 2 2 4 c-1 2-3 3-5 3 c-7-1-13-7-14-14 c0-2 1-4 2-6 z" fill="#fff"/>
    </svg>
    <span class="order-line__phone">555-418-2957</span>
  </footer>
</main>
</body>
</html>
```